Harlow peak Convenience store

I have just purchased a business you can see picture its very dated. It needs a fresh feel on top to say harlow peak Convenience store.
Underneath it could say something like groceries, fruit vegies and more. On the window it would be beter left clean on the top but at the bottom maybee pictures of fresh fruits vegetables and general items a high end gourmet feel
The photograph i have sent is the shop i purchased, and the old signage. Its very outdated i need it to be very clear and in date Added Wednesday, October 12, 2016
Im looking for it to have a more gourmet or high end feel Added Friday, October 14, 2016

```html
<!DOCTYPE html>
<html lang="en">
<head>
<meta charset="utf-8">
<title>Harlow Peak Convenience store – shopfront signage</title>
<link rel="stylesheet" href="https://fonts.googleapis.com/css2?family=Anton&family=Nanum+Pen+Script&display=swap">
<style>
  :root {
    --page: #ffffff;
    --facade: #5f5f5f;
    --panel: #ffffff;
    --panel-edge: #8a8a8a;
    --ink: #000000;
  }
  * { margin: 0; padding: 0; box-sizing: border-box; }
  html, body { width: 1200px; height: 1043px; overflow: hidden; background: var(--page); }
  .canvas { position: relative; width: 1200px; height: 1043px; }
  .facade { position: absolute; left: 66px; top: 130px; width: 1098px; height: 720px; background: var(--facade); }
  .panel { position: absolute; background: var(--panel); border: 1px solid var(--panel-edge); color: var(--ink); font-family: "Anton", "Oswald", sans-serif; }
  .store-name { left: 80px; top: 196px; width: 1036px; height: 107px; display: flex; align-items: center; padding-left: 10px; white-space: nowrap; }
  .store-name .name { font-size: 88px; line-height: 1; }
  .store-name .type { font-size: 50px; line-height: 1; margin-left: 30px; margin-top: 12px; }
  .tagline { left: 148px; top: 371px; width: 900px; height: 90px; display: flex; align-items: center; justify-content: center; font-size: 80px; line-height: 1; white-space: nowrap; }
  .hours { left: 244px; top: 494px; width: 299px; height: 293px; text-align: center; padding-top: 60px; font-size: 25px; line-height: 1.45; }
  .range { left: 599px; top: 491px; width: 449px; height: 292px; }
  .range .rule { position: absolute; left: 33px; width: 352px; height: 7px; background: var(--ink); }
  .range .rule.top { top: 16px; }
  .range .rule.bottom { top: 262px; }
  .range ul { list-style: none; position: absolute; left: 129px; top: 46px; font-size: 38px; line-height: 50px; }
  .note { position: absolute; font-family: "Nanum Pen Script", cursive; font-size: 72px; line-height: 1; color: var(--ink); }
  .note.white { left: 418px; top: 58px; }
  .note.transparent { left: 370px; top: 930px; }
  .arrows { position: absolute; left: 0; top: 0; }
  .arrows path { fill: none; stroke: var(--ink); stroke-width: 11; stroke-linecap: round; stroke-linejoin: round; }
</style>
</head>
<body>
<main class="canvas">
  <div class="facade"></div>

  <div class="panel store-name"><span class="name">Harlow Peak</span><span class="type">Convenience store</span></div>
  <div class="panel tagline">Groceries, fruit &amp; veg</div>
  <div class="panel hours"><p>We open evry day<br>7am - 7pm</p></div>
  <div class="panel range">
    <span class="rule top"></span>
    <ul>
      <li>Groceries</li>
      <li>fruit &amp; veg</li>
      <li>Bread</li>
      <li>Milk</li>
    </ul>
    <span class="rule bottom"></span>
  </div>

  <p class="note white">White</p>
  <p class="note transparent">Transparent</p>

  <svg class="arrows" width="1200" height="1043" viewBox="0 0 1200 1043" aria-hidden="true">
    <path d="M398 124 Q338 140 332 204"/>
    <path d="M314 178 L332 206 L356 180"/>
    <path d="M600 78 C880 76 1090 150 1136 270 C1160 340 1140 390 1078 372"/>
    <path d="M1098 350 L1072 372 L1104 392"/>
    <path d="M492 912 Q444 850 426 764"/>
    <path d="M410 790 L424 760 L452 780"/>
    <path d="M620 918 Q660 836 754 766"/>
    <path d="M728 768 L758 764 L754 794"/>
  </svg>
</main>
</body>
</html>
```